Online Training company needs a new website design (Wordpress)

We are looking for a new design for our website (run on WordPress). We currently have two websites (quizmarlow.com) and (velkorlearning.com) and are trying to combine them into a single design.

The site should contain the following sections (Start Here, courses, labs, practice exams, exam vouchers, books, articles, about us).

Start Here - With so many options on our site, we think it would be a good idea to have this page that will allow us to give students an overview of our different products/services and where to start when they first find out about our company.

Courses - These are our online video courses (products), currently hosted at velkorlearning.com. Each course has its own "product page".

Labs - These are online lab environments that a student can purchase. The layout for these would be similar to a course, but the purchase option will be different (our web developer will code all the back end stuff to make it work).

Practice Exams - This will allow students to take practice questions to study for their exams.

Exam Vouchers - Students can purchase their exam vouchers here at a discounted price for their certification exams.

Books - Will link to a page that displays our books that are available on Zorvel. (Examples of the covers are attached so you can see our current designs.)

Articles - This will be our "blog" area for us to post articles each week.

About Us - A short about us page describing our company.

***
As for the design of the page itself, we like the current color scheme at velkorlearning.com, but the layout isn't working well. It was fine when we just had video courses, but as we have added new products it is becoming more and more cumbersome.

I have been looking for inspiration around the web, and saw brightfernwealth.com as a good example of trying to provide focus to new users, while breaking out various parts of a business that contains 4-6 different product lines/topics. Another example of a site we like is lessonharborweb.com.

That said, we aren't looking to simply copy either site, and are completely open to recommendations and designs you may have.

Thank you and we look forward to working with you!

```html
<!DOCTYPE html>
<html lang="en">
<head>
<meta charset="utf-8">
<title>Velkor Learning</title>
<link href="https://fonts.googleapis.com/css2?family=Lato:wght@400;700;900&display=swap" rel="stylesheet">
<style>
:root{
  --navy:#1d4675;
  --blue:#2b5f9e;
  --ink:#222;
  --text:#555;
  --muted:#777;
  --grey-band:#f1f1f1;
  --line:#dcdcdc;
  --white:#fff;
  --gold:#f5a623;
}
*{box-sizing:border-box;margin:0;padding:0}
html,body{width:1200px;height:4489px;overflow:hidden}
body{font-family:'Lato',sans-serif;color:var(--text);background:var(--white);position:relative}
.abs{position:absolute}
.btn{position:absolute;background:var(--navy);color:var(--white);font-weight:700;font-size:15px;display:flex;align-items:center;justify-content:center;height:40px}
.section-title{position:absolute;left:0;width:1200px;text-align:center;font-size:26px;font-weight:700;color:var(--ink);letter-spacing:1px;text-transform:uppercase}
.section-title::after{content:"";display:block;width:56px;height:3px;background:var(--navy);margin:12px auto 0}
.band{position:absolute;left:0;width:1200px}
/* header */
.brand{position:absolute;left:75px;top:32px;display:flex;align-items:center;gap:12px}
.brand-mark{width:40px;height:40px;background:var(--navy)}
.brand-name{font-size:22px;font-weight:900;color:var(--navy);letter-spacing:1px;line-height:1}
.nav{position:absolute;right:72px;top:48px;display:flex;gap:28px;font-size:13px;font-weight:700;color:#333;text-transform:uppercase}
.nav .active{color:var(--blue)}
/* hero */
.hero{position:absolute;left:0;top:111px;width:1200px;height:549px;background:linear-gradient(120deg,#6d7a86,#b9a58e 45%,#8f8a84 70%,#5a6470)}
.hero-title{position:absolute;left:0;width:1200px;top:230px;text-align:center;color:var(--white);font-size:52px;font-weight:900;text-transform:uppercase;letter-spacing:1px}
.hero-sub{position:absolute;left:0;width:1200px;top:298px;text-align:center;color:var(--white);font-size:27px;font-weight:700}
.dots{position:absolute;top:502px;left:562px;display:flex;gap:10px}
.dots span{width:10px;height:10px;border-radius:50%;background:var(--white)}
.dots span.on{background:#3d82c4}
/* cards */
.card{position:absolute;width:330px;height:420px;border:1px solid var(--line);background:var(--white);text-align:center}
.card .pic{position:absolute;left:12px;top:12px;width:306px;height:176px}
.card h3{position:absolute;left:0;width:100%;top:208px;font-size:17px;font-weight:700;color:var(--blue)}
.card p{position:absolute;left:30px;width:270px;top:240px;font-size:13px;line-height:19px;color:var(--text)}
.card .price{position:absolute;left:0;width:100%;top:292px;font-size:30px;font-weight:900;color:var(--ink)}
.card .price sup{font-size:14px;vertical-align:top;position:relative;top:4px}
.card .price small{font-size:16px;font-weight:400}
.card .btn{left:72px;width:186px;top:348px}
.arrow{position:absolute;width:20px;height:30px}
/* features */
.feature h2{position:absolute;font-size:26px;font-weight:700;color:var(--ink);text-transform:uppercase}
.feature p{position:absolute;font-size:14px;line-height:22px;color:var(--text);width:520px}
/* books */
.book-cover{position:absolute;width:198px;height:300px}
.book-title{position:absolute;font-size:18px;font-weight:900;color:var(--navy);line-height:22px;text-transform:uppercase}
.book-text{position:absolute;font-size:13px;line-height:19px;width:260px}
.buy{position:absolute;width:228px;height:34px;border-radius:17px;background:var(--gold);border:2px solid #333;display:flex;align-items:center;padding-left:10px;gap:10px;font-size:14px;font-weight:700;color:var(--ink)}
.buy i{width:18px;height:18px;border-radius:50%;background:#222;display:block}
/* blog */
.post{position:absolute;width:330px}
.post h3{font-size:20px;font-weight:700;color:var(--blue);line-height:26px}
.post p{margin-top:14px;font-size:14px;line-height:21px;color:var(--text)}
.post a{display:block;margin-top:20px;font-size:14px;font-weight:700;color:var(--ink);text-decoration:none}
/* footer */
.foot-col{position:absolute;top:4290px;font-size:13px;color:var(--text);line-height:28px}
.foot-col h4{font-size:13px;font-weight:900;color:var(--navy);text-transform:uppercase;margin-bottom:6px;line-height:16px}
.social{display:flex;gap:14px;margin-top:10px}
.social span{width:20px;height:20px;border-radius:50%;background:#555;display:block}
</style>
</head>
<body>

<header>
  <div class="brand"><span class="brand-mark"></span><span class="brand-name">VELKOR<br>LEARNING</span></div>
  <nav class="nav"><span class="active">Home</span><span>Courses</span><span>Labs</span><span>Practice Exams</span><span>Exam Vouchers</span><span>Books</span><span>Articles</span><span>About Us</span></nav>
</header>

<section class="hero" role="img" aria-label="Photo of students studying together at laptops">
  <div class="hero-title">Aliquam Iaculis Massa</div>
  <div class="hero-sub">Quisque sit amet justo vestibulum, maximus sem et, fringilla lorem...</div>
  <div class="btn" style="left:512px;top:346px;width:176px">Get Started</div>
  <div class="dots"><span></span><span class="on"></span><span></span><span></span></div>
</section>

<!-- Courses -->
<div class="section-title" style="top:712px">Courses</div>
<svg class="arrow" style="left:42px;top:995px" viewBox="0 0 20 30"><path d="M15 3 4 15l11 12" fill="none" stroke="#777" stroke-width="3"/></svg>
<svg class="arrow" style="left:1138px;top:995px" viewBox="0 0 20 30"><path d="M5 3l11 12L5 27" fill="none" stroke="#777" stroke-width="3"/></svg>
<div class="card" style="left:78px;top:800px">
  <div class="pic" role="img" aria-label="Collage of course artwork for the full access plan" style="background:linear-gradient(135deg,#2d4e8c,#7b8fc4)"></div>
  <h3>Full Access to All Our Courses</h3><p>With our $9/month plan, you get unlimited access to all of our courses!</p>
  <div class="price"><sup>$</sup>9<small>/month</small></div><div class="btn">View Course</div>
</div>
<div class="card" style="left:435px;top:800px">
  <div class="pic" role="img" aria-label="Course artwork for the SVCFRAME Foundation course" style="background:linear-gradient(135deg,#1a2a4a,#3a5a8a)"></div>
  <h3>SVCFRAME Foundation (Exam Voucher)</h3><p>Purchase your discounted SVCFRAME Foundation exam voucher directly from Velkor Learning.</p>
  <div class="price"><sup>$</sup>299</div><div class="btn">View Course</div>
</div>
<div class="card" style="left:795px;top:800px">
  <div class="pic" role="img" aria-label="Course artwork for the PROJECTA Foundation course" style="background:linear-gradient(135deg,#1e3a6e,#4a6fb0)"></div>
  <h3>Full Access to All Our Courses</h3><p>With our $9/month plan, you get unlimited access to all of our courses!</p>
  <div class="price"><sup>$</sup>9<small>/month</small></div><div class="btn">View Course</div>
</div>

<!-- Labs -->
<div class="band" style="top:1284px;height:627px;background:var(--grey-band)"></div>
<div class="section-title" style="top:1342px">Labs</div>
<svg class="arrow" style="left:42px;top:1622px" viewBox="0 0 20 30"><path d="M15 3 4 15l11 12" fill="none" stroke="#777" stroke-width="3"/></svg>
<svg class="arrow" style="left:1138px;top:1622px" viewBox="0 0 20 30"><path d="M5 3l11 12L5 27" fill="none" stroke="#777" stroke-width="3"/></svg>
<div class="card" style="left:78px;top:1425px;height:426px">
  <div class="pic" role="img" aria-label="Photo of researchers working in a laboratory" style="height:196px;background:linear-gradient(135deg,#8fa6bf,#dfe6ee)"></div>
  <h3 style="top:222px">Full Access to All Our Courses</h3><p style="top:252px">With our $9/month plan, you get unlimited access to all of our courses!</p>
  <div class="price" style="top:302px"><sup>$</sup>9<small>/month</small></div><div class="btn" style="top:360px">View Details</div>
</div>
<div class="card" style="left:435px;top:1425px;height:426px">
  <div class="pic" role="img" aria-label="Photo of laboratory glassware under blue light" style="height:196px;background:linear-gradient(135deg,#0d3a6a,#3b8fd0)"></div>
  <h3 style="top:222px">SVCFRAME Foundation (Exam Voucher)</h3><p style="top:252px">Purchase your discounted SVCFRAME Foundation exam voucher directly from Velkor Learning.</p>
  <div class="price" style="top:302px"><sup>$</sup>299</div><div class="btn" style="top:360px">View Details</div>
</div>
<div class="card" style="left:795px;top:1425px;height:426px">
  <div class="pic" role="img" aria-label="Photo of scientists at a laboratory bench" style="height:196px;background:linear-gradient(135deg,#3c5a7a,#a9bccf)"></div>
  <h3 style="top:222px">Full Access to All Our Courses</h3><p style="top:252px">With our $9/month plan, you get unlimited access to all of our courses!</p>
  <div class="price" style="top:302px"><sup>$</sup>9<small>/month</small></div><div class="btn" style="top:360px">View Details</div>
</div>

<!-- Practice Exams -->
<section class="feature">
  <h2 style="left:75px;top:1972px">Practice Exams</h2>
  <p style="left:75px;top:2030px">Lorem ipsum dolor sit amet, consectetur adipiscing elit. Integer bibendum ipsum sit amet magna imperdiet consectetur. Etiam consectetur bibendum neque, id placerat dolor lobortis vel. Vestibulum ante ipsum primis in faucibus orci luctus et ultrices posuere cubilia. Duis volutpat ligula nibh, at efficitur enim luctus nec. Vestibulum lacinia cursus velit, dignissim cursus velit ultrices quis. Duis nec aliquet odio. Vestibulum vel tempor libero. Cras eleifend rhoncus dui ac semper.</p>
  <div class="btn" style="left:75px;top:2243px;width:236px">Take Practice Question</div>
  <div class="abs" role="img" aria-label="Photo of a student writing notes at a desk" style="left:615px;top:1970px;width:513px;height:330px;background:linear-gradient(135deg,#c9ced6,#f2f2f2 60%,#b8bcc4)"></div>
</section>
<div class="abs" style="left:75px;top:2347px;width:1053px;height:1px;background:var(--line)"></div>

<!-- Exam Vouchers -->
<section class="feature">
  <div class="abs" role="img" aria-label="Photo of two students celebrating at a laptop" style="left:78px;top:2390px;width:510px;height:330px;background:linear-gradient(135deg,#8a6b52,#d8c2a6 55%,#9a8a7c)"></div>
  <h2 style="left:612px;top:2392px">Exam Vouchers</h2>
  <p style="left:612px;top:2450px">Lorem ipsum dolor sit amet, consectetur adipiscing elit. Integer bibendum ipsum sit amet magna imperdiet consectetur. Etiam consectetur bibendum neque, id placerat dolor lobortis vel. Vestibulum ante ipsum primis in faucibus orci luctus et ultrices posuere cubilia. Duis volutpat ligula nibh, at efficitur enim luctus nec. Vestibulum lacinia cursus velit, dignissim cursus velit ultrices quis. Duis nec aliquet odio. Vestibulum vel tempor libero. Cras eleifend rhoncus dui ac semper.</p>
  <div class="btn" style="left:612px;top:2663px;width:240px">Get Your Exam Vouchers</div>
</section>

<!-- Books -->
<div class="band" style="top:2772px;height:483px;background:var(--grey-band)"></div>
<div class="section-title" style="top:2812px">Books</div>
<div class="book-cover" role="img" aria-label="Book cover for Quiz Marlow PROJECTA Foundation by Marcus Hale" style="left:78px;top:2898px;background:linear-gradient(180deg,#3b2a6b 0 14%,#f4f4f4 14% 100%)"></div>
<div class="book-title" style="left:312px;top:2945px">PROJECTA<br>Foundation</div>
<div class="book-text" style="left:312px;top:2996px">Lorem ipsum dolor sit amet, consectetur adipiscing elit tincidunt vestibulum tempor ...</div>
<div class="buy" style="left:312px;top:3082px"><i></i>Buy from Zorvel</div>
<div class="book-cover" role="img" aria-label="Book cover for Quiz Marlow SVCFRAME Foundation by Marcus Hale" style="left:615px;top:2898px;background:linear-gradient(180deg,#1d6e9a 0 14%,#f4f4f4 14% 100%)"></div>
<div class="book-text" style="left:858px;top:2996px;color:#ccc">Lorem ipsum dolor sit amet, consectetur adipiscing elit tincidunt vestibulum tempor ...</div>
<div class="buy" style="left:858px;top:3082px"><i></i>Buy from Zorvel</div>

<!-- Blog -->
<div class="section-title" style="top:3297px">Blog Posts</div>
<article class="post" style="left:78px;top:3380px"><h3>Continual Service Improvement Model</h3><p>The final improvement model covered by the SVCFRAME Foundations exam is called the Continual Service Improvement Mode. This model is a simple set of guiding questions used to organize and perpetuate an improvement program within a service management organization.</p><a>Read More &rsaquo;&rsaquo;</a></article>
<article class="post" style="left:435px;top:3380px"><h3>7-Step Process Improvement Process</h3><p>The final improvement model covered by the SVCFRAME Foundations exam is called the Continual Service Improvement Mode. This model is a simple set of guiding questions used to organize and perpetuate an improvement program within a service management organization.</p><a>Read More &rsaquo;&rsaquo;</a></article>
<article class="post" style="left:795px;top:3380px"><h3>Continual Service Improvement (Csi) Phase</h3><p>The final improvement model covered by the SVCFRAME Foundations exam is called the Continual Service Improvement Mode. This model is a simple set of guiding questions used to organize and perpetuate an improvement program within a service management organization.</p><a>Read More &rsaquo;&rsaquo;</a></article>
<div class="btn" style="left:520px;top:3683px;width:160px">Read All Posts</div>

<!-- About -->
<div class="band" style="top:3805px;height:455px;background:var(--grey-band)"></div>
<div class="section-title" style="top:3862px">About Us</div>
<p class="abs" style="left:95px;top:3930px;width:1010px;text-align:center;font-size:14px;line-height:22px">Lorem ipsum dolor sit amet, consectetur adipiscing elit. Integer bibendum ipsum sit amet magna imperdiet consectetur. Etiam consectetur bibendum neque, id placerat dolor lobortis vel. Vestibulum ante ipsum primis in faucibus orci luctus et ultrices posuere cubilia. Duis volutpat ligula nibh, at efficitur enim luctus nec. Vestibulum lacinia cursus velit, dignissim cursus velit ultrices quis. Duis nec aliquet odio. Vestibulum vel tempor libero. Cras eleifend rhoncus dui ac semper.<br>Duis a sapien urna. Aliquam sed vestibulum leo. Nulla ac vestibulum eros, dignissim dictum diam. Ut volutpat lacus et sodales finibusaliquam fermentum turpis pretium tellus bibendum varius.</p>
<div class="btn" style="left:520px;top:4135px;width:160px">Read More</div>

<!-- Footer -->
<footer>
  <div class="brand" style="top:4300px;left:78px"><span class="brand-mark"></span><span class="brand-name">VELKOR<br>LEARNING</span></div>
  <div class="abs" style="left:78px;top:4395px;font-size:12px;line-height:20px;color:var(--muted)">Copyright © 2018, Company Name.<br>All Right reserved</div>
  <div class="foot-col" style="left:342px"><h4>Site Map</h4>Home<br>Courses<br>Labs<br>Practice Exams<br>Exam Vouchers</div>
  <div class="foot-col" style="left:507px"><h4>&nbsp;</h4>Books<br>Articles<br>About Us</div>
  <div class="foot-col" style="left:618px"><h4>Email Sign Up</h4>
    <div style="width:238px;height:36px;border:1px solid var(--line);font-size:12px;color:var(--muted);padding:0 10px;line-height:34px;margin-top:6px">Enter Email Address</div>
    <div class="btn" style="position:static;width:100px;height:36px;margin:12px 0 0 138px;font-size:13px">SIGN UP</div>
  </div>
  <div class="foot-col" style="left:909px"><h4>Follow Us</h4><div class="social"><span></span><span></span><span></span><span></span><span></span></div></div>
</footer>

</body>
</html>
```